Website For Ladder Company

I have a client that needs a new look to a stale website. Notes:

They like the the grays and reds of bruvell.com

i like the layout of this theme so i can get them a responsive design but it is a little too clean / white and needs some more color. I like this font and typography style http://fenmarkcraftworks.com/

They like the layout of zolt.com but not black

Current site is halvesby.com but I want to make sure you work directly through me and NOT CONTACT THE CLIENT DIRECTLY

There needs to be a blog feed section, place for featured video, intro paragraph and get all their current navigation.

there will be no flash on the site but a similar way they have the different types of ladder categories should be integrated

I envisioned this image in the header in some fashion http://www.pixdravenbank.com/cat.mhtml?searchterm=on+a+ladder&search_group=&lang=en&search_source=search_form#id=472910386&src=81c_4KHtrQZ2MopYdnWkEsA-3-30 with a tagline over it saying

Now Would Be a Good Time to Know What Ladder You Use. Trust Halvesby.

Industry/Entity Type

Fashion

```html
<!DOCTYPE html>
<html lang="en">
<head>
<meta charset="utf-8">
<title>Halvesby — Ladders</title>
<link href="https://fonts.googleapis.com/css2?family=Open+Sans:wght@400;600;700&family=PT+Sans+Narrow:wght@400;700&display=swap" rel="stylesheet">
<style>
:root{
  --red:#e0191b;
  --red-dark:#b51214;
  --ink:#333;
  --muted:#7a7a7a;
  --light:#f1f1f1;
  --band:#e4e4e4;
  --dark:#3a3a3a;
  --darker:#262626;
  --white:#fff;
}
*{box-sizing:border-box;margin:0;padding:0}
html,body{width:1200px;height:2660px;overflow:hidden}
body{font-family:"Open Sans",Arial,sans-serif;font-size:11px;color:var(--ink);background:var(--white);line-height:1.6}
.wrap{width:840px;margin:0 auto;position:relative;height:100%}
h2,h3,h4{font-family:"PT Sans Narrow","Arial Narrow",sans-serif;text-transform:uppercase;font-weight:700}
.red{color:var(--red)}

/* top bar */
.topbar{height:40px;background:var(--white);border-bottom:1px solid #e5e5e5}
.topbar .wrap{display:flex;align-items:center;gap:40px}
.topbar .contact{display:flex;align-items:center;gap:8px;color:var(--muted)}
.topbar .search{position:absolute;right:-180px;top:0;height:40px;width:240px;background:var(--darker);color:#aaa;padding:11px 40px;font-size:11px}

/* header */
.header{height:110px;background:var(--white)}
.header .wrap{display:flex;align-items:center;justify-content:space-between}
.brand small{display:block;font-size:8px;color:var(--muted);letter-spacing:1px;text-transform:uppercase}
.brand span{font-family:"Open Sans",sans-serif;font-size:40px;font-weight:700;color:var(--red);line-height:1}
.nav{display:flex;gap:26px;font-size:10px;font-weight:700;text-transform:uppercase}
.nav a{color:var(--ink);text-decoration:none;padding-bottom:6px}
.nav a.active{color:var(--red);border-bottom:2px solid var(--red)}

/* hero */
.hero{height:440px;position:relative;background:linear-gradient(90deg,#0b1c2e 0%,#13263c 40%,#2b2b2b 70%,#1a1a1a 100%)}
.hero .photo{position:absolute;left:0;top:0;width:620px;height:440px;background:radial-gradient(circle at 55% 50%,#4aa0e0 0%,#1a4c7c 25%,#0d2238 55%,transparent 80%)}
.hero .copy{position:absolute;left:780px;top:90px;width:330px;color:#ddd}
.hero h1{font-family:"PT Sans Narrow",sans-serif;font-size:30px;line-height:1.1;color:var(--red);text-transform:uppercase;margin-bottom:18px}
.hero p{font-size:12px;margin-bottom:26px}
.more{display:inline-flex;align-items:center;gap:8px;font-size:11px;color:inherit}
.dot{width:14px;height:14px;border-radius:50%;background:var(--red);display:inline-flex;align-items:center;justify-content:center}

/* features */
.features{height:310px;background:var(--light);border-top:10px solid var(--white)}
.features .wrap{display:flex;justify-content:space-between;padding-top:60px}
.feature{width:250px;text-align:center}
.feature .icon{width:72px;height:72px;border-radius:50%;background:var(--red);margin:0 auto 22px;display:flex;align-items:center;justify-content:center;box-shadow:0 0 0 5px #fff}
.feature h3{font-size:17px;margin-bottom:8px}
.feature p{color:var(--muted);font-size:10px}

/* products */
.products{height:280px;background:var(--band);border-top:1px solid #d4d4d4}
.products .wrap{display:flex;gap:30px;padding-top:50px}
.products .intro{width:190px}
.products h2{font-size:17px;color:var(--red);margin-bottom:8px}
.products .intro p{color:var(--muted);font-size:10px;margin-bottom:12px}
.product{width:190px;text-align:center}
.product .pic{height:120px;background:linear-gradient(160deg,#9a9a9a,#d6d6d6)}
.product:nth-child(3) .pic{background:linear-gradient(160deg,#7f7f7f,#c9c9c9)}
.product:nth-child(4) .pic{background:linear-gradient(160deg,#b74a3a,#dcdcdc)}
.price{font-size:20px;color:var(--red);font-weight:700;margin-top:10px}

/* callout */
.callout{height:150px;background:var(--white)}
.callout .box{position:absolute;top:50px;left:0;width:840px;height:70px;border:1px solid #ddd;box-shadow:0 2px 4px rgba(0,0,0,.1);display:flex;align-items:center;padding-left:20px}
.callout p{color:var(--red);font-weight:700;font-size:10px;text-transform:uppercase;width:560px}
.callout .btn{position:absolute;right:-1px;top:-1px;height:70px;width:150px;background:var(--red);color:#fff;font-family:"PT Sans Narrow",sans-serif;font-weight:700;font-size:17px;display:flex;align-items:center;justify-content:center}

/* why */
.why{height:280px;border-top:1px solid #e3e3e3}
.why .wrap{display:flex;padding-top:50px}
.why h2{font-size:15px;color:var(--red);width:180px}
.why .grid{display:grid;grid-template-columns:1fr 1fr;gap:40px 60px;width:660px}
.reason{display:flex;gap:14px}
.reason .icon{flex:none;width:36px;height:36px;border-radius:50%;background:#555;display:flex;align-items:center;justify-content:center}
.reason h4{font-size:12px;margin-bottom:4px}
.reason p{color:var(--muted);font-size:10px}

/* news */
.news{height:220px;background:var(--band)}
.news h2{font-size:15px;color:var(--red);padding-top:26px;margin-bottom:12px}
.news .row{display:flex;gap:10px}
.news .pic{width:200px;height:110px;background:linear-gradient(160deg,#8a8a8a,#d2d2d2)}
.news .pic.video{position:relative;background:linear-gradient(160deg,#c8c8c8,#efefef)}
.news .pic.video .dot{position:absolute;left:82px;top:37px;width:36px;height:36px}
.news .lead{width:200px;height:110px;background:var(--red);color:#fff;padding:14px}
.news .lead h3{font-size:13px;line-height:1.2;margin-bottom:6px}
.news .lead p{font-size:9px}

/* columns */
.columns{height:290px}
.columns .wrap{display:flex;gap:30px;padding-top:30px}
.col{width:260px}
.col h4{font-size:12px;border-bottom:1px solid #ddd;padding-bottom:6px;margin-bottom:14px}
.post{display:flex;gap:10px;margin-bottom:16px}
.post .date{flex:none;width:34px;height:34px;background:var(--red);color:#fff;font-weight:700;text-align:center;font-size:12px;line-height:34px}
.post .date.grey{background:#999}
.post b{color:var(--red);font-size:10px;display:block}
.post p{color:var(--muted);font-size:9px}
.feat{display:flex;gap:10px;align-items:center;font-size:10px;color:var(--muted);margin-bottom:12px}
.feat .sq{flex:none;width:14px;height:14px;background:var(--red)}
.feat .sq.grey{background:#bbb}
.feat.on{color:var(--red)}
.quote{background:var(--red);color:#fff;padding:14px;font-size:10px;position:relative}
.quote:after{content:"";position:absolute;right:30px;bottom:-10px;border:10px solid transparent;border-top-color:var(--red);border-bottom:0}
.author{text-align:right;margin-top:16px;font-size:10px}
.author b{display:block}

/* partners */
.partners{height:200px;border-top:1px solid #e3e3e3}
.partners h2{font-size:13px;color:var(--red);padding-top:26px;margin-bottom:30px}
.partners .row{display:flex;justify-content:space-between;align-items:center;padding:0 20px}
.partner{display:flex;align-items:center;gap:8px;font-size:26px;font-weight:700;color:#444}
.partner i{width:22px;height:22px;background:#444;display:block}

/* footer */
.footer{height:300px;background:var(--dark);color:#bbb}
.footer .wrap{display:flex;gap:40px;padding-top:40px}
.footer h4{font-size:13px;color:#fff;margin-bottom:12px}
.footer p{font-size:10px}
.footer .c1{width:190px}.footer .c2{width:180px}.footer .c3{width:230px}.footer .c4{width:150px}
.tweet{display:flex;gap:8px;margin-bottom:10px;font-size:9px}
.tweet i{flex:none;width:24px;height:24px;background:#555;border-radius:2px}
.map{height:110px;background:radial-gradient(ellipse at center,#f2f2f2 0%,#dcdcdc 55%,transparent 70%)}
.bottom{height:40px;background:var(--darker);color:#999;font-size:9px}
.bottom .wrap{display:flex;align-items:center;justify-content:space-between}
.bottom .links{display:flex;gap:18px}
.bottom .social{display:flex;gap:6px}
.bottom .social i{width:12px;height:12px;border-radius:50%;background:var(--red);display:block}
</style>
</head>
<body>

<div class="topbar"><div class="wrap">
  <div class="contact"><svg width="12" height="12" viewBox="0 0 12 12"><path d="M3 1l2 2-1 2 3 3 2-1 2 2-2 2C5 11 1 7 1 3z" fill="#e0191b"/></svg>+1 (555) 014 7720</div>
  <div class="contact"><svg width="12" height="10" viewBox="0 0 12 10"><rect x="0.5" y="0.5" width="11" height="9" fill="none" stroke="#e0191b"/><path d="M1 1l5 4 5-4" fill="none" stroke="#e0191b"/></svg>info@halvesby.com</div>
  <div class="contact"><svg width="12" height="12" viewBox="0 0 12 12"><circle cx="6" cy="6" r="5" fill="#e0191b"/></svg>live chat</div>
  <div class="search">Search...</div>
</div></div>

<header class="header"><div class="wrap">
  <div class="brand"><small>Ladders for every height</small><span>Halvesby</span></div>
  <nav class="nav">
    <a class="active">Home</a><a>About Us</a><a>Products</a><a>Features</a><a>Trade Shows</a><a>FAQs</a><a>Contact Us</a>
  </nav>
</div></header>

<section class="hero">
  <div class="photo" role="img" aria-label="Hands holding a glowing blue globe"></div>
  <div class="copy">
    <h1>Lorem ipsum dolar omnis explicabo sit ipsao</h1>
    <p>Aspernatur magni aperiam omnis explicabo nemo enim voluptas sit aut odit aut fugit sed quia.</p>
    <a class="more">read more <span class="dot"><svg width="6" height="6" viewBox="0 0 6 6"><path d="M1 0l4 3-4 3z" fill="#fff"/></svg></span></a>
  </div>
</section>

<section class="features"><div class="wrap">
  <div class="feature"><div class="icon"><svg width="30" height="30" viewBox="0 0 30 30"><circle cx="15" cy="15" r="11" fill="none" stroke="#fff" stroke-width="3"/><path d="M15 8v7h6" stroke="#fff" stroke-width="3" fill="none"/></svg></div>
    <h3>Aperiam aut</h3><p>Sed ut perspiciatis unde omnis iste natus error sit voluptatem accusantium doloremque laudantium totam rem aperiam.</p></div>
  <div class="feature"><div class="icon"><svg width="30" height="30" viewBox="0 0 30 30"><path d="M6 11l9 9 9-9" stroke="#fff" stroke-width="4" fill="none"/></svg></div>
    <h3>Perspiciatis beatae</h3><p>Nemo enim ipsam voluptatem quia voluptas sit aspernatur aut odit aut fugit sed quia magni dolores eos.</p></div>
  <div class="feature"><div class="icon"><svg width="30" height="30" viewBox="0 0 30 30"><path d="M6 15l6 6 12-12" stroke="#fff" stroke-width="4" fill="none"/></svg></div>
    <h3>Quae aperiam</h3><p>Neque porro quisquam est qui dolorem ipsum quia dolor sit amet consectetur adipisci velit sed quia non.</p></div>
</div></section>

<section class="products"><div class="wrap">
  <div class="intro"><h2>Popular product</h2><p>Ut enim ad minima veniam quis nostrum exercitationem ullam corporis suscipit laboriosam nisi ut aliquid.</p>
    <a class="more">view more <span class="dot"><svg width="6" height="6" viewBox="0 0 6 6"><path d="M1 0l4 3-4 3z" fill="#fff"/></svg></span></a></div>
  <div class="product"><div class="pic" role="img" aria-label="Worker on a ladder against a grey wall"></div><div class="price">$ 543.00</div></div>
  <div class="product"><div class="pic" role="img" aria-label="Painter standing on a step ladder"></div><div class="price">$ 543.00</div></div>
  <div class="product"><div class="pic" role="img" aria-label="Worker in red climbing a ladder"></div><div class="price">$ 543.00</div></div>
</div></section>

<section class="callout"><div class="wrap">
  <div class="box"><p>Sed quia accusantium laudantium inventore ipsa sit eiust qui et ipsao</p><div class="btn">EXPLICABO</div></div>
</div></section>

<section class="why"><div class="wrap">
  <h2>Why choose us</h2>
  <div class="grid">
    <div class="reason"><div class="icon"><svg width="16" height="16" viewBox="0 0 16 16"><path d="M3 8l3 3 7-7" stroke="#fff" stroke-width="2" fill="none"/></svg></div><div><h4>Persip beatae quia</h4><p>At vero eos et accusamus et iusto odio dignissimos ducimus qui blanditiis praesentium.</p></div></div>
    <div class="reason"><div class="icon"><svg width="16" height="16" viewBox="0 0 16 16"><circle cx="8" cy="8" r="5" fill="none" stroke="#fff" stroke-width="2"/></svg></div><div><h4>Persip beatae quia</h4><p>Temporibus autem quibusdam et aut officiis debitis aut rerum necessitatibus saepe.</p></div></div>
    <div class="reason"><div class="icon"><svg width="16" height="16" viewBox="0 0 16 16"><path d="M3 13l10-10M9 3h4v4" stroke="#fff" stroke-width="2" fill="none"/></svg></div><div><h4>Persip beatae quia</h4><p>Itaque earum rerum hic tenetur a sapiente delectus ut aut reiciendis voluptatibus.</p></div></div>
    <div class="reason"><div class="icon"><svg width="16" height="16" viewBox="0 0 16 16"><path d="M8 2v12M2 8h12" stroke="#fff" stroke-width="2"/></svg></div><div><h4>Persip beatae quia</h4><p>Nam libero tempore cum soluta nobis est eligendi optio cumque nihil impedit quo.</p></div></div>
  </div>
</div></section>

<section class="news"><div class="wrap">
  <h2>Recent news</h2>
  <div class="row">
    <div class="pic video" role="img" aria-label="Featured video still of a worker on a ladder"><span class="dot"><svg width="14" height="14" viewBox="0 0 6 6"><path d="M1 0l4 3-4 3z" fill="#fff"/></svg></span></div>
    <div class="pic" role="img" aria-label="Team meeting in an office"></div>
    <div class="pic" role="img" aria-label="Builders reviewing plans on site"></div>
    <div class="lead"><h3>Ipsum consequatur quia consequuntur</h3><p>Quis autem vel eum iure reprehenderit qui in ea voluptate velit esse quam nihil.</p></div>
  </div>
</div></section>

<section class="columns"><div class="wrap">
  <div class="col"><h4>Recent posts</h4>
    <div class="post"><div class="date">26</div><div><b>Veritatis beatae aut sunt voluptas</b><p>Omnis voluptas assumenda est omnis dolor repellendus temporibus.</p></div></div>
    <div class="post"><div class="date grey">24</div><div><b>Perspiciatis unde omnis iste natus</b><p>Ratione voluptatem sequi nesciunt neque porro quisquam est.</p></div></div>
    <a class="more">Read more <span class="dot"><svg width="6" height="6" viewBox="0 0 6 6"><path d="M1 0l4 3-4 3z" fill="#fff"/></svg></span></a>
  </div>
  <div class="col"><h4>Best features</h4>
    <div class="feat"><i class="sq grey"></i>Voluptatem sequi nesciunt</div>
    <div class="feat"><i class="sq grey"></i>Neque porro quisquam est</div>
    <div class="feat on"><i class="sq"></i>Dolorem ipsum quia dolor sit amet</div>
    <div class="feat"><i class="sq grey"></i>Adipisci velit sed quia non</div>
    <div class="feat"><i class="sq grey"></i>Numquam eius modi tempora</div>
    <div class="feat"><i class="sq grey"></i>Incidunt ut labore et dolore</div>
  </div>
  <div class="col"><h4>Our testimonials</h4>
    <div class="quote">Voluptatem accusantium doloremque laudantium totam rem aperiam eaque ipsa quae ab illo inventore veritatis.</div>
    <div class="author"><b>Adam Vale</b>Site Manager</div>
  </div>
</div></section>

<section class="partners"><div class="wrap">
  <h2>Best partner</h2>
  <div class="row">
    <div class="partner"><i></i>Norvale</div>
    <div class="partner">Kestra</div>
    <div class="partner">Lumora</div>
    <div class="partner">Brightfold</div>
    <div class="partner"><i></i>Pelto</div>
  </div>
</div></section>

<footer class="footer"><div class="wrap">
  <div class="c1"><h4>About us</h4><p>Fugit sed dict omnis explicabo nemo enim ipsam voluptatem quia voluptas sit aspernatur aut odit aut fugit consequuntur magni.</p><br><a class="more">Read more <span class="dot"><svg width="6" height="6" viewBox="0 0 6 6"><path d="M1 0l4 3-4 3z" fill="#fff"/></svg></span></a></div>
  <div class="c2"><h4>Adress</h4><p>PO Box 218<br>Wrenfield Lane 40<br>Marlow Bay 3107<br>+1 (555) 014 7720<br><br>Search in map</p></div>
  <div class="c3"><h4>Recent tweets</h4>
    <div class="tweet"><i></i><p>@halvesby new step range lands next week, lorem ipsum dolor.</p></div>
    <div class="tweet"><i></i><p>@halvesby safety tips for tall jobs, quia voluptas sit.</p></div>
    <div class="tweet"><i></i><p>@halvesby see us at the trade show, nemo enim ipsam.</p></div>
  </div>
  <div class="c4"><h4>Business maps</h4><div class="map" role="img" aria-label="Map of the regions where the business operates"></div></div>
</div></footer>

<div class="bottom"><div class="wrap">
  <span>© 2013 HALVESBY. All Rights Reserved.</span>
  <div class="links"><span>about us</span><span>customer service</span><span>privacy policy</span><span>contact us</span></div>
  <div class="social"><i></i><i></i><i></i><i></i><i></i></div>
</div></div>

</body>
</html>
```